Vent doux

Hello,
I’m a designer sunglasses reatail Store owner in Montreal, Quebec.

Looking for something modern, fresh with a trendy appeal.

Will send my logo.
Thank you.

Store

```html
<!DOCTYPE html>
<html lang="fr">
<head>
<meta charset="utf-8">
<title>Vent doux — cartes professionnelles</title>
<link rel="stylesheet" href="https://fonts.googleapis.com/css2?family=Open+Sans:wght@400;600;700&display=swap">
<style>
  :root {
    --backdrop: #5c5d5f;
    --card-dark: #060606;
    --card-light: #f1f1f1;
    --brand-red: #a3162b;
    --ink: #1d1d1d;
    --white: #ffffff;
  }
  html, body {
    margin: 0;
    padding: 0;
    width: 1200px;
    height: 904px;
    overflow: hidden;
    background: var(--backdrop);
    font-family: "Open Sans", Arial, sans-serif;
  }
  .canvas {
    position: relative;
    width: 1200px;
    height: 904px;
  }
  .card {
    position: absolute;
    width: 560px;
    height: 320px;
    border-radius: 3px;
    overflow: hidden;
    box-shadow: 0 10px 24px rgba(0,0,0,0.35);
  }
  .card--front {
    left: 100px;
    top: 120px;
    background: var(--card-dark);
    display: flex;
    align-items: center;
    justify-content: center;
  }
  .card--back {
    left: 540px;
    top: 470px;
    background: var(--card-light);
  }
  .wordmark {
    display: flex;
    align-items: center;
    gap: 10px;
  }
  .wordmark__dot {
    width: 14px;
    height: 14px;
    border-radius: 50%;
    background: var(--brand-red);
    flex: none;
  }
  .wordmark__name {
    font-weight: 600;
    font-size: 34px;
    letter-spacing: 2px;
    text-transform: uppercase;
    line-height: 1;
    white-space: nowrap;
  }
  .card--front .wordmark__name { color: var(--white); }
  .card--back .wordmark {
    position: absolute;
    left: 60px;
    top: 42px;
  }
  .card--back .wordmark__dot { width: 11px; height: 11px; }
  .card--back .wordmark__name { color: var(--ink); font-size: 24px; }
  .contact {
    position: absolute;
    left: 110px;
    top: 112px;
    color: var(--ink);
  }
  .contact__name {
    margin: 0;
    font-weight: 700;
    font-size: 19px;
    line-height: 1.3;
    color: var(--brand-red);
  }
  .contact__role {
    margin: 0 0 14px 0;
    font-size: 14px;
    line-height: 1.35;
  }
  .contact__address {
    margin: 0 0 14px 0;
    font-style: normal;
    font-size: 14px;
    line-height: 1.35;
  }
  .contact__list {
    list-style: none;
    margin: 0;
    padding: 0;
    font-size: 14px;
  }
  .contact__list li {
    display: flex;
    align-items: center;
    gap: 10px;
    line-height: 22px;
    white-space: nowrap;
  }
  .contact__icon { width: 14px; height: 14px; flex: none; }
</style>
</head>
<body>
<main class="canvas">
  <section class="card card--front" aria-label="Recto de la carte">
    <div class="wordmark">
      <span class="wordmark__dot"></span>
      <span class="wordmark__name">Vent doux</span>
    </div>
  </section>

  <section class="card card--back" aria-label="Verso de la carte">
    <div class="wordmark">
      <span class="wordmark__dot"></span>
      <span class="wordmark__name">Vent doux</span>
    </div>

    <div class="contact">
      <p class="contact__name">Léa Marchand</p>
      <p class="contact__role">Manager</p>
      <address class="contact__address">210 rue Saint-Paul Ouest<br>Montréal, QC H2Y 1Z8</address>
      <ul class="contact__list">
        <li>
          <svg class="contact__icon" viewBox="0 0 16 16" aria-hidden="true"><circle cx="8" cy="8" r="8" fill="#a3162b"/><path d="M5 4.5c.6-.4 1.2 0 1.4.6l.3.9c.1.4 0 .7-.3.9l-.4.3c.4.9 1.1 1.6 2 2l.3-.4c.2-.3.5-.4.9-.3l.9.3c.6.2 1 .8.6 1.4-.5.8-1.4 1-2.2.7C6.6 10.2 5.8 9.4 5 7.6c-.3-.9-.6-2.3 0-3.1z" fill="#fff"/></svg>
          +1 514 555 0148
        </li>
        <li>
          <svg class="contact__icon" viewBox="0 0 16 16" aria-hidden="true"><circle cx="8" cy="8" r="8" fill="#a3162b"/><rect x="4" y="5.2" width="8" height="5.6" rx="0.6" fill="#fff"/><path d="M4.3 5.5 8 8.3l3.7-2.8" fill="none" stroke="#a3162b" stroke-width="0.9"/></svg>
          bonjour@ventdoux.ca
        </li>
        <li>
          <svg class="contact__icon" viewBox="0 0 16 16" aria-hidden="true"><circle cx="8" cy="8" r="8" fill="#a3162b"/><g fill="none" stroke="#fff" stroke-width="0.9"><circle cx="8" cy="8" r="4"/><ellipse cx="8" cy="8" rx="1.8" ry="4"/><path d="M4 8h8"/></g></svg>
          www.ventdoux.ca
        </li>
      </ul>
    </div>
  </section>
</main>
</body>
</html>
```